Speech Pathology card for parents of young children

I need a professional, yet fun card for my speech and language pathology services.
I'm trying to offer my speech therapy services to parents of young children. These parents will most likely be women. I want the card to have a fun feel to it and have a concept of speech and language in it (kind of like the cartoon I've attached below showing a boy/girl talking).

I'd want a white background on the card and to bring in some bright colors as well.

Please include the KROV logo in a smaller size on a free corner of the card.

Target Market(s)

parents of young children

Contact Information for Business Card

must have my information and I'd like it to have the KROV logo (small) somewhere in the corner)

Font styles to use
Serif
Sans Serif

Colors

Designer to choose colors to be used in the design.

Requirements
Must have
• The card title should read: Speech-Language Pathologist
• Rosalind Pettry
• MS CCC-SLP/TSSLD (this under the name)
• 415 906 2283
• rosiepettry@kelvormail.net
Nice to have
• i'm looking for a card with a white background and a fun icon that encompasses speaking... similar to the one I've attached.

```html
<!DOCTYPE html>
<html lang="en">
<head>
<meta charset="utf-8">
<title>Rosalind Pettry – Speech-Language Pathologist</title>
<link rel="stylesheet" href="https://fonts.googleapis.com/css2?family=Roboto:wght@300;400;500&display=swap">
<style>
  :root {
    --page-bg: #e9e7e3;
    --card-white: #ffffff;
    --accent-orange: #f0a51e;
    --accent-teal: #12a9c6;
    --accent-pink: #e5197f;
    --text-grey: #55585c;
    --text-dark: #3a3c3f;
    --mark-grey: #4a4c50;
  }
  * { box-sizing: border-box; margin: 0; padding: 0; }
  html, body {
    width: 1200px;
    height: 1023px;
    overflow: hidden;
    background: var(--page-bg);
    font-family: "Roboto", Arial, sans-serif;
  }
  .card {
    position: absolute;
    left: 100px;
    top: 226px;
    width: 1000px;
    height: 571px;
    background: var(--card-white);
    box-shadow: 0 10px 30px rgba(0,0,0,0.12);
    overflow: hidden;
  }
  .corner-swoosh {
    position: absolute;
    left: 0;
    top: 0;
    width: 1000px;
    height: 571px;
  }
  .speaking-illustration {
    position: absolute;
    left: 56px;
    top: 92px;
    width: 180px;
    height: 160px;
    border-radius: 14px;
    background: linear-gradient(135deg, #fbe3c4 0%, #f3f3f3 45%, #d6f0e0 100%);
  }
  .web-address {
    position: absolute;
    left: 252px;
    top: 70px;
    font-size: 19px;
    font-weight: 500;
    color: var(--accent-pink);
  }
  .association-mark {
    position: absolute;
    left: 60px;
    top: 288px;
    display: flex;
    align-items: center;
    gap: 14px;
  }
  .association-mark .mark-dot {
    width: 52px;
    height: 52px;
    border-radius: 50%;
    background: var(--mark-grey);
  }
  .association-mark .mark-name {
    font-size: 20px;
    font-weight: 400;
    color: var(--mark-grey);
    letter-spacing: 2px;
  }
  .identity {
    position: absolute;
    right: 230px;
    top: 110px;
    text-align: right;
  }
  .identity .person-name {
    font-size: 44px;
    font-weight: 500;
    color: var(--accent-orange);
    line-height: 1.1;
  }
  .identity .credentials {
    font-size: 24px;
    font-weight: 300;
    color: var(--text-dark);
    letter-spacing: 0.5px;
    margin-top: 6px;
  }
  .identity .role-title {
    font-size: 20px;
    font-weight: 400;
    color: var(--accent-teal);
    margin-top: 8px;
  }
  .divider-rule {
    position: absolute;
    left: 60px;
    width: 720px;
    top: 376px;
    height: 2px;
    background: var(--accent-orange);
  }
  .contact-list {
    position: absolute;
    left: 62px;
    top: 400px;
    list-style: none;
  }
  .contact-list li {
    display: flex;
    align-items: center;
    gap: 12px;
    font-size: 25px;
    font-weight: 300;
    color: var(--text-grey);
    height: 40px;
  }
  .contact-list svg { width: 18px; height: 18px; flex: none; }
</style>
</head>
<body>
  <div class="card">
    <svg class="corner-swoosh" viewBox="0 0 1000 571" aria-hidden="true">
      <path d="M700 571 C 800 430, 880 200, 1000 20 L 1000 571 Z" fill="var(--accent-orange)"/>
      <path d="M736 571 C 830 440, 905 220, 1000 62 L 1000 571 Z" fill="var(--card-white)"/>
      <path d="M744 571 C 838 444, 912 228, 1000 74 L 1000 571 Z" fill="var(--accent-teal)"/>
    </svg>

    <div class="speaking-illustration" role="img" aria-label="Sketched child calling out through a colourful megaphone"></div>
    <div class="web-address">talkbloom.net</div>

    <div class="association-mark">
      <span class="mark-dot"></span>
      <span class="mark-name">KROV</span>
    </div>

    <div class="identity">
      <div class="person-name">Rosalind Pettry</div>
      <div class="credentials">MS CCC-SLP/TSSLD</div>
      <div class="role-title">Speech-Language Pathologist</div>
    </div>

    <div class="divider-rule"></div>

    <ul class="contact-list">
      <li>
        <svg viewBox="0 0 24 24" aria-hidden="true"><path d="M6.6 10.8a15.1 15.1 0 0 0 6.6 6.6l2.2-2.2a1 1 0 0 1 1-.25 11.4 11.4 0 0 0 3.6.57 1 1 0 0 1 1 1V20a1 1 0 0 1-1 1A17 17 0 0 1 3 4a1 1 0 0 1 1-1h3.5a1 1 0 0 1 1 1c0 1.25.2 2.45.57 3.57a1 1 0 0 1-.25 1z" fill="var(--accent-orange)"/></svg>
        415 906 2283
      </li>
      <li>
        <svg viewBox="0 0 24 24" aria-hidden="true"><rect x="3" y="5" width="18" height="14" rx="1.5" fill="none" stroke="var(--accent-orange)" stroke-width="2"/><path d="M3.5 6l8.5 7 8.5-7" fill="none" stroke="var(--accent-orange)" stroke-width="2"/></svg>
        rosiepettry@kelvormail.net
      </li>
    </ul>
  </div>
</body>
</html>
```